Author needs eye catching business card design

I need a design that depicts an item from my book Venthe. This item is a blue stone that houses a dragon soul in it. You can vaguely see the shape of a dragon spiraling around the stone in a shimmering blue-silver hue. I've attached my concept design. I've also attached a bookmark concept design to help inspire. I also have attached a picture of a stone that is the color that the stones in my book are. On the back I would like something nice looking but blank for the most part - a space for me to write on if I want. On the front of the card I would like the following stacked upon each other : Fantasy Author, Clara Dovrek, www.cdovrek.com

Contact Information for Business Card

Font styles to use
Serif
Script

Requirements
Must have
• 1 Dragon wisp swirling around inside the stone. I have attached my concept drawing for inspiration.
• The following text stacked upon each other: Fantasy Author, Clara Dovrek, www.cdovrek.com, c_dovrek@mailbrook.net
• The symbols for Glimboard, Lumora, Kinlyst, and Quillet followed by "@claraedovrek"
Should not have
• The exact picture of the stone picture I have attached. This is for color and size/shape inspiration only and is not my own personal picture.
• No pink please.

```html
<!DOCTYPE html>
<html lang="en">
<head>
<meta charset="utf-8">
<title>Clara Dovrek – Business Card</title>
<link rel="stylesheet" href="https://fonts.googleapis.com/css2?family=Great+Vibes&family=Lora:wght@400;600&display=swap">
<style>
  :root {
    --stage: #2e2f31;
    --card: #ffffff;
    --cyan: #3fb3d3;
    --navy: #2d2b7c;
    --ink: #3a3880;
    --rule: #9a9aa6;
    --crystal-a: #4fb8dc;
    --crystal-b: #2f74b8;
    --crystal-c: #7a78c4;
  }
  * { box-sizing: border-box; margin: 0; padding: 0; }
  html, body {
    width: 1200px; height: 900px; overflow: hidden;
    background: var(--stage);
    font-family: "Lora", serif;
  }
  .card {
    position: absolute;
    width: 600px; height: 343px;
    background: var(--card);
    border-radius: 3px;
    overflow: hidden;
  }
  .card--back { left: 80px; top: 70px; }
  .card--front { left: 520px; top: 480px; }

  /* back */
  .back-emblem {
    position: absolute; left: 200px; top: 40px;
    width: 200px; height: 250px;
    border-radius: 50%;
    background: radial-gradient(ellipse at center, rgba(79,184,220,0.18), rgba(122,120,196,0.08) 60%, rgba(255,255,255,0) 75%);
  }
  .write-lines { position: absolute; left: 120px; top: 110px; width: 370px; }
  .write-lines span {
    display: block; height: 0; margin-bottom: 50px;
    border-top: 1.5px dashed var(--rule);
  }

  /* front */
  .crystal-mark {
    position: absolute; left: 420px; top: 24px;
    width: 130px; height: 130px;
    border-radius: 18px;
    background: linear-gradient(135deg, var(--crystal-a), var(--crystal-b) 55%, var(--crystal-c));
    opacity: 0.9;
  }
  .identity { position: absolute; left: 40px; top: 136px; }
  .identity__name {
    font-family: "Great Vibes", cursive;
    color: var(--cyan); font-weight: 400; font-size: 40px; line-height: 1.05;
  }
  .identity__role {
    color: var(--ink); font-size: 17px; line-height: 1.3;
  }
  .divider {
    position: absolute; left: 40px; right: 0; top: 206px;
    height: 2px; background: var(--navy);
  }
  .contacts { position: absolute; left: 40px; top: 216px; list-style: none; }
  .contacts li {
    display: flex; align-items: center; gap: 10px;
    color: var(--ink); font-size: 15px; line-height: 27px;
  }
  .contacts svg { width: 15px; height: 15px; flex: none; }

  .details {
    position: absolute; right: 30px; top: 218px;
    text-align: right; color: var(--navy);
  }
  .address { font-size: 14px; line-height: 19px; }
  .socials {
    display: grid; grid-template-columns: auto auto;
    column-gap: 14px; justify-content: end;
    margin-top: 6px; list-style: none;
  }
  .socials li {
    display: flex; align-items: center; gap: 5px;
    font-size: 13px; line-height: 17px; color: var(--ink);
  }
  .socials li::before {
    content: ""; width: 8px; height: 8px; border-radius: 50%;
    background: var(--cyan); flex: none;
  }
  .handle { font-size: 13px; line-height: 18px; color: var(--ink); }

  .base-band {
    position: absolute; left: 0; right: 0; bottom: 0;
    height: 8px; background: var(--navy);
  }
  .base-accent {
    position: absolute; right: 0; bottom: 8px;
    width: 60px; height: 10px; background: var(--cyan);
  }
</style>
</head>
<body>

<section class="card card--back" aria-label="Card back">
  <div class="back-emblem" role="img" aria-label="Faint crystal shard emblem"></div>
  <div class="write-lines"><span></span><span></span><span></span><span></span></div>
</section>

<section class="card card--front" aria-label="Card front">
  <div class="crystal-mark" role="img" aria-label="Blue crystal shards emblem"></div>

  <div class="identity">
    <p class="identity__name">Clara Dovrek</p>
    <p class="identity__role">Fantasy Author</p>
  </div>

  <div class="divider"></div>

  <ul class="contacts">
    <li>
      <svg viewBox="0 0 16 16" aria-hidden="true"><path fill="#3fb3d3" d="M3.2 1.5l2.3 2.4-1.3 1.8c.9 2 2.6 3.7 4.6 4.6l1.8-1.3 2.4 2.3-1.5 2.2C6.5 13.3 2.7 9.5 1 4.5z"/></svg>
      555-014-2100
    </li>
    <li>
      <svg viewBox="0 0 16 16" aria-hidden="true"><rect x="1" y="3" width="14" height="10" rx="1" fill="#3fb3d3"/><path d="M1.5 3.6L8 9l6.5-5.4" fill="none" stroke="#fff" stroke-width="1.3"/></svg>
      c_dovrek@mailbrook.net
    </li>
    <li>
      <svg viewBox="0 0 16 16" aria-hidden="true"><circle cx="8" cy="8" r="7" fill="#3fb3d3"/><path d="M1.5 8h13M8 1.2c-2.4 2-2.4 11.6 0 13.6M8 1.2c2.4 2 2.4 11.6 0 13.6" fill="none" stroke="#fff" stroke-width="1.1"/></svg>
      www.cdovrek.com
    </li>
  </ul>

  <div class="details">
    <p class="address">Your address, city,<br>state, ZIP 00000</p>
    <ul class="socials">
      <li>Glimboard</li>
      <li>Lumora</li>
      <li>Kinlyst</li>
      <li>Quillet</li>
    </ul>
    <p class="handle">@claraedovrek</p>
  </div>

  <div class="base-accent"></div>
  <div class="base-band"></div>
</section>

</body>
</html>
```